The title of the book is: Resonant Foundations for Builders
I need a front and back cover for my new book.
This is a reference book written to teach architects the basics of acoustics and sound.
The subtitle is: The handbook on echoes and tone most designers hoped their teachers had given them
Author is: Dorian Wick
Publisher: PLOV Press
Primary colors desired are deep red, and deep rich gold. A splash of cobalt blue might be nice too.
Black and/or White fonts
I'm a fan of art deco designs, but I'm also a minimalist, so I'd like something that's not too busy.
This will be used for both a paperback and ebook. Format for "portrait" viewing.
Final files need to be high-res .jpg. Size: 1873 pixels on the longest side, 1600 pixels on the shortest side (350 dpi)
The inside cover page is attached as a reference only.

Target Market(s)

Architects

Industry/Entity Type

Architecture, interior design, and pro audio

Font styles to use
Sans Serif
Other font styles liked:
• Arial

Colors
0054AA
0677BA
7BADD7
CADEEF
E8F1F8
FFC000
F8CF3A
FAE287
FDF2CF
FEFAEE
EB3D1F
EC4F4E
F09395
F8D3D4
FCEDEE

Requirements
Must have
• Elegant font cover design
Nice to have
• Spine and back cover design to compliment front cover. Spine will be roughly 1/2"
Should not have
• Anything that will date the book based on front cover graphics

```html
<!DOCTYPE html>
<html lang="en">
<head>
<meta charset="utf-8">
<title>Resonant Foundations for Builders — Cover Spread</title>
<link rel="stylesheet" href="https://fonts.googleapis.com/css2?family=Fira+Sans+Condensed:wght@500;600&family=Questrial&family=Russo+One&display=swap">
<style>
  :root {
    --cobalt: #006eb8;
    --deep-red: #a12439;
    --shadow-red: #7e2731;
    --gold: #be9a70;
    --paper: #ffffff;
    --ink: #1e1e1e;
    --press-grey: #8a8a8a;
    --spire-dark: #bdbdbd;
    --spire-mid: #dcdcdc;
    --spire-light: #e4e4e4;
  }
  html, body {
    margin: 0;
    padding: 0;
    width: 1200px;
    height: 792px;
    overflow: hidden;
    background: var(--cobalt);
  }
  .cover-spread { display: block; width: 1200px; height: 792px; }
  .bg-cobalt { fill: var(--cobalt); }
  .bg-red { fill: var(--deep-red); }
  .spire-shadow { fill: var(--shadow-red); }
  .bg-paper { fill: var(--paper); }
  .rule-gold { fill: var(--gold); }
  .rule-cobalt { fill: var(--cobalt); }
  .spire-dark { fill: var(--spire-dark); }
  .spire-mid { fill: var(--spire-mid); }
  .spire-light { fill: var(--spire-light); }
  .author-square { fill: var(--deep-red); }

  .publisher-back {
    font-family: "Fira Sans Condensed", sans-serif;
    font-weight: 600; font-size: 34px; letter-spacing: 3px;
    fill: var(--paper);
  }
  .publisher-front {
    font-family: "Fira Sans Condensed", sans-serif;
    font-weight: 600; font-size: 37px;
    fill: var(--press-grey);
  }
  .initial {
    font-family: "Russo One", sans-serif;
  }
  .initial-back { font-size: 150px; fill: var(--paper); }
  .initial-front { font-size: 298px; fill: var(--deep-red); }
  .title {
    font-family: "Questrial", sans-serif;
  }
  .title-back { fill: var(--paper); }
  .title-front { fill: var(--ink); }
  .author-back {
    font-family: "Fira Sans Condensed", sans-serif;
    font-weight: 600; font-size: 36px;
    fill: var(--gold);
  }
  .author-front {
    font-family: "Fira Sans Condensed", sans-serif;
    font-weight: 600; font-size: 48px;
    fill: var(--paper);
  }
  .tagline {
    font-family: "Fira Sans Condensed", sans-serif;
    font-weight: 600; font-size: 18px;
  }
  .tagline-back { fill: var(--paper); }
  .tagline-front { fill: var(--ink); font-weight: 500; }
</style>
</head>
<body>
<svg class="cover-spread" viewBox="0 0 1200 792" xmlns="http://www.w3.org/2000/svg">
  <rect class="bg-cobalt" x="0" y="0" width="1200" height="792"/>

  <!-- Back cover -->
  <g class="back-cover">
    <polygon class="bg-red" points="240,0 586,0 586,792 0,792 0,616 91,616 91,33 240,33"/>
    <polygon class="spire-shadow" points="480,35 569,616 480,616"/>

    <rect class="rule-gold" x="172" y="96" width="219" height="10"/>
    <text class="publisher-back" x="175" y="148">PLOV Press</text>

    <text class="initial initial-back" x="170" y="283">R</text>
    <text class="author-back" x="274" y="208">Dorian</text>
    <text class="author-back" x="274" y="244">Wick</text>
    <text class="title title-back" x="273" y="283" font-size="28" textLength="118" lengthAdjust="spacingAndGlyphs">ESONANT</text>
    <text class="title title-back" x="172" y="326" textLength="219" lengthAdjust="spacingAndGlyphs"><tspan font-size="42">F</tspan><tspan font-size="31">OUNDATIONS</tspan></text>
    <text class="title title-back" x="172" y="367" textLength="219" lengthAdjust="spacingAndGlyphs"><tspan font-size="31">FOR </tspan><tspan font-size="42">B</tspan><tspan font-size="31">UILDERS</tspan></text>
    <rect class="rule-gold" x="172" y="381" width="219" height="10"/>

    <text class="tagline tagline-back" x="172" y="420">The handbook on echoes and tone</text>
    <text class="tagline tagline-back" x="172" y="443">most designers hoped their</text>
    <text class="tagline tagline-back" x="172" y="466">teachers had given them</text>
  </g>

  <!-- Front cover -->
  <g class="front-cover">
    <polygon class="bg-paper" points="640,0 896,0 896,36 1028,36 1028,85 1077,85 1077,171 1200,171 1200,616 640,616"/>

    <rect class="rule-cobalt" x="706" y="44" width="88" height="10"/>
    <text class="publisher-front" x="703" y="93">PLOV</text>
    <text class="publisher-front" x="703" y="127">Press</text>

    <polygon class="spire-dark" points="905,173 928,317 905,317"/>
    <polygon class="spire-mid" points="972,36 1016,317 972,317"/>
    <polygon class="spire-light" points="1076,173 1099,317 1076,317"/>

    <text class="initial initial-front" x="709" y="382">R</text>
    <text class="title title-front" x="908" y="381" font-size="60" textLength="245" lengthAdjust="spacingAndGlyphs">ESONANT</text>
    <text class="title title-front" x="706" y="466" textLength="440" lengthAdjust="spacingAndGlyphs"><tspan font-size="96">F</tspan><tspan font-size="72">OUNDATIONS</tspan></text>
    <text class="title title-front" x="706" y="547" textLength="470" lengthAdjust="spacingAndGlyphs"><tspan font-size="72">FOR </tspan><tspan font-size="96">B</tspan><tspan font-size="72">UILDERS</tspan></text>

    <text class="tagline tagline-front" x="709" y="578">The handbook on echoes and tone most designers hoped their</text>
    <text class="tagline tagline-front" x="709" y="601">teachers had given them</text>

    <rect class="author-square" x="715" y="642" width="56" height="35"/>
    <text class="author-front" x="787" y="677">Dorian Wick</text>
  </g>
</svg>
</body>
</html>
```